Corporate Two Sided Business Card

Looking for a Corporate "edgy" Modern look and feel for a business card

We are looking at two options. Dark background with our logo on it, white background with our logo on it - The background is more - Charcoal / Graphite then black

Details will be

Danielle Forsk

Licensee / Director

m. 0428 519 064

e. danielle@quorvela.com.au

quorvela.com.au

Target Market(s)

Professional Business people that refer use business and clients that own Investment Properties

Industry/Entity Type

Business

Contact Information for Business Card

Details will be

Danielle Forsk

Licensee / Director

m. 0428 519 064

quorvela.com.au

Font styles to use
Serif

Colors
000000
ec1f27
eeeeee
ffffff

Requirements
Must have
• Two options - White Background and Dark Background. - Two sided
Nice to have
• A design that is edgy, modern and new to look instead of boring style corporate cards - It should be a full integrated design
Should not have
• Block looking - Cheap.

```html
<!DOCTYPE html>
<html lang="en">
<head>
<meta charset="utf-8">
<title>Quorvela – Business Card</title>
<link href="https://fonts.googleapis.com/css2?family=Source+Sans+3:wght@400;600;700&display=swap" rel="stylesheet">
<style>
  :root {
    --stage: #111111;
    --card-light: #e4e3e1;
    --card-dark: #252525;
    --brand-red: #ec1f27;
    --wordmark-grey: #4a4a4a;
    --wordmark-dark: #565656;
    --ink: #1e1e1e;
    --ink-soft: #3a3a3a;
  }
  * { margin: 0; padding: 0; box-sizing: border-box; }
  html, body {
    width: 1200px; height: 900px; overflow: hidden;
    background: var(--stage);
    font-family: "Source Sans 3", "Myriad Pro", Arial, sans-serif;
  }
  .stage { position: relative; width: 1200px; height: 900px; }
  .card {
    position: absolute; top: 170px; width: 347px; height: 561px;
    overflow: hidden;
    box-shadow: 2px 3px 6px rgba(0,0,0,0.55);
  }
  .card--front { left: 259px; background: var(--card-light); }
  .card--back { left: 631px; background: var(--card-dark); }

  .brand {
    position: absolute; top: 151px; left: 0; width: 100%; height: 44px;
    display: flex; align-items: center; justify-content: center; gap: 9px;
  }
  .brand__square { width: 26px; height: 26px; background: var(--brand-red); }
  .brand__name {
    font-size: 44px; font-weight: 600; color: var(--wordmark-grey);
    letter-spacing: 0.5px; line-height: 1;
  }

  .contact {
    position: absolute; top: 370px; left: 0; width: 100%;
    text-align: center; color: var(--ink);
  }
  .contact__name {
    font-size: 21px; font-weight: 700; color: var(--brand-red);
    text-transform: uppercase; line-height: 23px;
  }
  .contact__role { font-size: 15px; line-height: 19px; color: var(--ink-soft); margin-top: 1px; }
  .contact__icons {
    display: flex; justify-content: center; gap: 7px; margin: 25px 0 10px;
  }
  .contact__icons svg { width: 13px; height: 13px; fill: var(--brand-red); }
  .contact__line { font-size: 15px; line-height: 20.5px; }

  .back-mark {
    position: absolute; left: 150px; top: 150px;
    writing-mode: vertical-rl; transform: rotate(180deg);
    display: flex; align-items: center; gap: 14px;
  }
  .back-mark__name {
    font-size: 72px; font-weight: 600; color: var(--wordmark-dark);
    line-height: 1; letter-spacing: 1px;
  }
  .back-mark__square { width: 40px; height: 40px; background: var(--brand-red); }
</style>
</head>
<body>
<main class="stage">
  <section class="card card--front" aria-label="Card front">
    <div class="brand">
      <span class="brand__square"></span>
      <span class="brand__name">quorvela</span>
    </div>
    <div class="contact">
      <p class="contact__name">Danielle Forsk</p>
      <p class="contact__role">Licensee / Director</p>
      <div class="contact__icons">
        <svg viewBox="0 0 16 16" aria-label="Mobile"><path d="M4 0h8a1 1 0 0 1 1 1v14a1 1 0 0 1-1 1H4a1 1 0 0 1-1-1V1a1 1 0 0 1 1-1zm1 2v10h6V2zm3 11a1 1 0 1 0 0 2 1 1 0 0 0 0-2z"/></svg>
        <svg viewBox="0 0 16 16" aria-label="Email"><path d="M0 3h16v10H0zm1.5 1.2V12h13V4.2L8 9z"/></svg>
        <svg viewBox="0 0 16 16" aria-label="Website"><path d="M8 0a8 8 0 1 0 0 16A8 8 0 0 0 8 0zm-1 2.2v3.2H4.2A6 6 0 0 1 7 2.2zm2 0a6 6 0 0 1 2.8 3.2H9zM2.3 7.2H7v1.6H2.3a6 6 0 0 1 0-1.6zm6.7 0h4.7a6 6 0 0 1 0 1.6H9zM4.2 10.6H7v3.2a6 6 0 0 1-2.8-3.2zm4.8 0h2.8A6 6 0 0 1 9 13.8z"/></svg>
      </div>
      <p class="contact__line">0428 519 064</p>
      <p class="contact__line">danielle@quorvela.com.au</p>
      <p class="contact__line">www.quorvela.com.au</p>
    </div>
  </section>

  <section class="card card--back" aria-label="Card back">
    <div class="back-mark">
      <span class="back-mark__square"></span>
      <span class="back-mark__name">quorvela</span>
    </div>
  </section>
</main>
</body>
</html>
```